Lowell Brandt

20 Year Licensed Master Barber specializing in:
men/women cuts, Grooming, Straight razor Shaving and tape line enhancement, beard grooming, eye brow enhancement, South of France, Hot Towel Treatments, Scalp, Blow outs, Shags, Custom Design,RazorCuts,Shear Cuts, Bobs, Perms, Relaxers, Shoe Shine.
Please create a wonderful business card incorporating all the info above and selecting one of the photos. Please be creative.

Barber

```html
<!DOCTYPE html>
<html lang="pt">
<head>
<meta charset="utf-8">
<title>Lowell Brandt – Business Card</title>
<link href="https://fonts.googleapis.com/css2?family=Cinzel:wght@400;600;700&display=swap" rel="stylesheet">
<style>
  :root {
    --page-bg: #e7e4df;
    --card-frost: rgba(232, 234, 234, 0.9);
    --card-frost-dark: #c9cccc;
    --card-band: rgba(255, 255, 255, 0.55);
    --card-edge: #b9bcbf;
    --card-edge-light: #f4f5f6;
    --circle-blue: #2e3187;
    --circle-ring: #b4343a;
    --name-gold: #e6b63c;
    --text-white: #ffffff;
    --badge-blue: #2e3187;
  }
  * { box-sizing: border-box; margin: 0; padding: 0; }
  html, body {
    width: 1070px; height: 1200px; overflow: hidden;
    background: var(--page-bg);
    font-family: "Cinzel", "Times New Roman", serif;
  }
  .canvas { position: relative; width: 1070px; height: 1200px; }

  .card {
    position: absolute;
    width: 790px; height: 462px;
    background: linear-gradient(180deg, var(--card-frost) 0%, var(--card-frost-dark) 100%);
    border: 6px solid var(--card-edge);
    box-shadow: inset 0 0 0 2px var(--card-edge-light), 0 6px 18px rgba(0,0,0,0.12);
    overflow: hidden;
  }
  .card--front { left: 138px; top: 116px; border-radius: 8px 231px 231px 8px / 8px 231px 231px 8px; }
  .card--back  { left: 138px; top: 652px; border-radius: 231px 8px 8px 231px / 231px 8px 8px 231px; }

  .card__band {
    position: absolute; left: 0; right: 0; top: 150px; height: 170px;
    background: var(--card-band);
  }

  .seal {
    position: absolute; width: 160px; height: 160px;
    display: flex; flex-direction: column; align-items: center; justify-content: center; gap: 10px;
  }
  .seal__dot {
    width: 70px; height: 70px; border-radius: 50%;
    background: var(--badge-blue);
  }
  .seal__name {
    font-weight: 700; font-size: 19px; color: var(--badge-blue);
    letter-spacing: 1px; white-space: nowrap;
  }
  .card--front .seal { left: 78px; top: 144px; }
  .card--back .seal  { left: 506px; top: 142px; }

  .disc {
    position: absolute; width: 320px; height: 320px; border-radius: 50%;
    background: var(--circle-blue);
    border: 6px solid var(--circle-ring);
    box-shadow: 0 0 0 3px rgba(255,255,255,0.35);
    color: var(--text-white);
  }
  .card--front .disc { left: 380px; top: 55px; }
  .card--back .disc  { left: 85px; top: 51px; }

  .contact {
    list-style: none; position: absolute; left: 14px; top: 98px;
    font-size: 14.5px; line-height: 22px; letter-spacing: 0.2px; white-space: nowrap;
  }
  .contact li { display: flex; align-items: flex-start; gap: 7px; }
  .contact .icon { flex: 0 0 14px; width: 14px; height: 14px; margin-top: 4px; }
  .contact .indent { padding-left: 21px; }

  .identity {
    position: absolute; left: 0; right: 0; top: 124px; text-align: center;
  }
  .identity__name { font-size: 30px; font-weight: 700; letter-spacing: 0.5px; white-space: nowrap; }
  .identity__name .first { color: var(--name-gold); }
  .identity__name .last  { color: var(--text-white); }
  .identity__role { font-size: 23px; font-weight: 600; color: var(--text-white); margin-top: 2px; letter-spacing: 0.5px; }
</style>
</head>
<body>
<main class="canvas">

  <section class="card card--front">
    <div class="card__band"></div>
    <div class="seal">
      <span class="seal__dot"></span>
      <span class="seal__name">Lowell Brandt</span>
    </div>
    <div class="disc">
      <ul class="contact">
        <li>
          <svg class="icon" viewBox="0 0 14 14"><circle cx="7" cy="7" r="7" fill="#fff"/><path d="M7 3a2.4 2.4 0 0 0-2.4 2.4C4.6 7.3 7 10.6 7 10.6s2.4-3.3 2.4-5.2A2.4 2.4 0 0 0 7 3z" fill="#2e3187"/></svg>
          <span>Rua das Palmeiras, 1270</span>
        </li>
        <li class="indent">Sala 804 8º andar Centro</li>
        <li class="indent">Vila Serena SP</li>
        <li>
          <svg class="icon" viewBox="0 0 14 14"><circle cx="7" cy="7" r="7" fill="#fff"/><path d="M4.6 3.6l1.3 1.3-.7 1a5 5 0 0 0 2.9 2.9l1-.7 1.3 1.3-1 1.1C6.6 10.3 3.7 7.4 3.5 4.6z" fill="#2e3187"/></svg>
          <span>(11)3456-7812</span>
        </li>
        <li>
          <svg class="icon" viewBox="0 0 14 14"><circle cx="7" cy="7" r="7" fill="#fff"/><rect x="4.6" y="3" width="4.8" height="8" rx="0.8" fill="#2e3187"/></svg>
          <span>11 9234-5570</span>
        </li>
        <li>
          <svg class="icon" viewBox="0 0 14 14"><circle cx="7" cy="7" r="7" fill="#fff"/><rect x="3.4" y="4.4" width="7.2" height="5.2" fill="#2e3187"/><path d="M3.6 4.6L7 7.4l3.4-2.8" stroke="#fff" stroke-width="0.8" fill="none"/></svg>
          <span>lowell.brandt@mailbox.com</span>
        </li>
        <li>
          <svg class="icon" viewBox="0 0 14 14"><circle cx="7" cy="7" r="7" fill="#fff"/><circle cx="7" cy="7" r="3.6" fill="none" stroke="#2e3187" stroke-width="0.9"/><path d="M3.4 7h7.2M7 3.4c-1.6 2-1.6 5.2 0 7.2M7 3.4c1.6 2 1.6 5.2 0 7.2" stroke="#2e3187" stroke-width="0.8" fill="none"/></svg>
          <span>www.brandtbarbearia.com.br</span>
        </li>
      </ul>
    </div>
  </section>

  <section class="card card--back">
    <div class="card__band"></div>
    <div class="disc">
      <div class="identity">
        <h1 class="identity__name"><span class="first">Lowell</span> <span class="last">Brandt</span></h1>
        <p class="identity__role">Owner / C.E.O.</p>
      </div>
    </div>
    <div class="seal">
      <span class="seal__dot"></span>
      <span class="seal__name">Lowell Brandt</span>
    </div>
  </section>

</main>
</body>
</html>
```